mailer to distressed properties

Our business is a company that buys houses for cash that are in need of repairs. Need to create a post card to mail to homeowners to get them to call us to give them a price on their home for cash and purchase it. Would like a run down house on background and our company info so they could call us. Have a logo would like to incorporate in it. Want to get to the point across we can buy there home for cash on any condition and close quickly. We can also buy them if they have permit or violation issues. We also buy homes going into foreclosure so we can stop foreclosure. Company name is R & T Dwellings. P o box 829 Fernwick my 10472. 555-214-8693. Email us at info@rntdwellings.example and our website Rntdwellings.example. Open to a lot of direct designs excited to see what you come up with. Anything else you can think we are open to see it. Email us with any other questions . Also can add fast closing and save no real estate commissions collected. We want it in color your choice. Also on font open to anything and size of font.

Target Market(s)

Run down and distressed properties

Industry/Entity Type

Construction Company

Font styles to use
Serif
Sans Serif

Requirements
Must have
• A background of a distressed home and our info how to call us
Nice to have
• Colorful and attractive
Should not have
• Nothing I can think of

```html
<!DOCTYPE html>
<html lang="en">
<head>
<meta charset="utf-8">
<title>R &amp; T Dwellings – Postcard Mailer</title>
<link href="https://fonts.googleapis.com/css2?family=Roboto+Condensed:ital,wght@0,400;0,700;0,900;1,900&family=Open+Sans:wght@400;600&display=swap" rel="stylesheet">
<style>
  :root{
    --bg:#e9e9e9;
    --paper:#ffffff;
    --red:#e0232a;
    --green:#7cc242;
    --blue:#2f5fb8;
    --ink:#1d1d1d;
    --dark:#232323;
    --grey:#555;
    --photo-green:#5f8a3c;
    --photo-sky:#9fbf7a;
  }
  *{box-sizing:border-box;margin:0;padding:0}
  html,body{width:1200px;height:1200px;overflow:hidden;background:var(--bg)}
  .card{position:absolute;left:180px;width:840px;height:540px;background:var(--paper);overflow:hidden;box-shadow:0 2px 6px rgba(0,0,0,.15)}
  .card--front{top:40px}
  .card--back{top:620px}
  .card svg.shapes{position:absolute;inset:0}
  .brand{position:absolute;font-family:"Roboto Condensed",sans-serif;font-weight:900;color:var(--ink);display:flex;align-items:center;gap:8px}
  .brand__mark{width:22px;height:22px;background:var(--ink)}
  .front__brand{left:34px;top:26px;font-size:26px}
  .brand-rule{position:absolute;left:34px;top:70px;width:230px;height:4px;background:var(--red);border-bottom:2px solid var(--blue)}
  .headline{position:absolute;left:34px;top:92px;font-family:"Roboto Condensed",sans-serif;font-weight:900;line-height:.95;text-transform:uppercase}
  .headline__l1{font-size:38px;color:var(--blue)}
  .headline__l2{font-size:56px;color:var(--green)}
  .headline__l3{font-size:50px;color:var(--ink)}
  .call-band{position:absolute;left:0;top:262px;height:52px;width:470px;background:var(--blue);clip-path:polygon(0 0,94% 0,100% 100%,0 100%);color:#fff;font-family:"Roboto Condensed",sans-serif;font-weight:900;font-size:30px;display:flex;align-items:center;padding-left:34px;gap:18px}
  .cta{position:absolute;left:34px;top:330px;font-family:"Roboto Condensed",sans-serif;font-weight:900;text-transform:uppercase}
  .cta__small{font-size:34px;color:var(--green)}
  .cta__big{font-size:52px;color:var(--red)}
  .website{position:absolute;left:30px;top:489px;font-family:"Open Sans",sans-serif;font-size:15px;letter-spacing:6px;color:#ddd}
  .photo{position:absolute}
  .photo--house{inset:0;clip-path:polygon(300px 0,840px 0,840px 384px,560px 434px);background:linear-gradient(180deg,#3f6b2a 0%,var(--photo-green) 45%,#8a939c 60%,var(--photo-sky) 100%)}
  .photo--person{left:640px;top:250px;width:170px;height:290px;background:linear-gradient(180deg,#c9b8a8 0%,#c8cde0 30%,#9aa3b8 70%,#6f6f72 100%);border-radius:70px 70px 0 0}
  .badge{position:absolute;left:436px;top:318px;width:126px;height:126px;border-radius:50%;background:var(--red);border:5px solid var(--green);box-shadow:0 0 0 3px #fff inset;color:#fff;font-family:"Roboto Condensed",sans-serif;font-weight:900;text-transform:uppercase;display:flex;flex-direction:column;align-items:center;justify-content:center;line-height:.9;text-align:center}
  .badge__no{font-size:40px}
  .badge__sub{font-size:13px}

  .photo--model{left:130px;top:0;width:300px;height:115px;background:linear-gradient(135deg,#d9d3cb 0%,#b08a5c 45%,#f1f1f1 100%);opacity:.8;clip-path:polygon(12% 0,100% 0,100% 55%,78% 100%,0 85%)}
  .photo--interior{left:0;top:380px;width:300px;height:160px;background:linear-gradient(180deg,rgba(215,215,215,.6),rgba(255,255,255,0));clip-path:polygon(0 0,100% 90%,0 100%)}
  .back__brand{left:470px;top:74px;font-size:28px}
  .about{position:absolute;left:36px;top:118px;width:430px;font-family:"Open Sans",sans-serif;color:var(--grey);font-size:11.5px;line-height:1.35}
  .about__title{font-family:"Roboto Condensed",sans-serif;font-weight:700;color:var(--red);font-size:24px;line-height:1.1;margin-bottom:4px}
  .about__text{margin-bottom:5px}
  .contacts{list-style:none;font-size:11.5px;line-height:1.4;margin-top:4px}
  .contacts li{display:flex;align-items:center;gap:6px}
  .contacts svg{width:10px;height:10px;flex:none}
  .stamp{position:absolute;left:700px;top:215px;width:90px;height:96px;background:var(--dark)}
</style>
</head>
<body>

<section class="card card--front">
  <div class="photo photo--house" role="img" aria-label="Photo of a weathered two-storey house among green trees"></div>
  <svg class="shapes" width="840" height="540" viewBox="0 0 840 540" aria-hidden="true">
    <polyline points="290,0 552,444 840,392" fill="none" stroke="var(--red)" stroke-width="9"/>
    <polyline points="274,0 540,454 840,402" fill="none" stroke="var(--green)" stroke-width="6"/>
    <polyline points="260,0 528,464 840,412" fill="none" stroke="var(--blue)" stroke-width="6"/>
    <line x1="0" y1="468" x2="520" y2="468" stroke="var(--green)" stroke-width="3"/>
    <polygon points="0,474 516,474 552,540 0,540" fill="var(--dark)"/>
  </svg>
  <div class="photo photo--person" role="img" aria-label="Photo of a smiling company representative in shirt and tie gesturing toward the house"></div>

  <div class="brand front__brand"><span class="brand__mark"></span>R &amp; T Dwellings</div>
  <div class="brand-rule"></div>
  <h1 class="headline">
    <div class="headline__l1">Quickly Sell</div>
    <div class="headline__l2">Your House</div>
    <div class="headline__l3">Fast for Cash</div>
  </h1>
  <div class="call-band"><span>CALL US AT</span><span>555-214-8693</span></div>
  <div class="cta"><span class="cta__small">To Get </span><span class="cta__big">Started!</span></div>
  <div class="website">www.rntdwellings.example</div>
  <div class="badge"><span class="badge__no">NO</span><span class="badge__sub">Real Estate<br>Commissions</span></div>
</section>

<section class="card card--back">
  <div class="photo photo--model" role="img" aria-label="Illustration of a house under renovation with blueprints"></div>
  <div class="photo photo--interior" role="img" aria-label="Faded photo of a bright living room interior"></div>
  <svg class="shapes" width="840" height="540" viewBox="0 0 840 540" aria-hidden="true">
    <polyline points="0,362 262,484 840,58" fill="none" stroke="var(--red)" stroke-width="10"/>
    <polyline points="0,378 262,500 840,74" fill="none" stroke="var(--green)" stroke-width="6"/>
    <polyline points="0,392 262,514 840,88" fill="none" stroke="var(--blue)" stroke-width="6"/>
  </svg>

  <div class="brand back__brand"><span class="brand__mark"></span>R &amp; T Dwellings</div>
  <div class="about">
    <h2 class="about__title">About Us</h2>
    <p class="about__text">R &amp; T Dwellings understands the challenges homeowners face when trying to sell their house. If you want to avoid the lengthy process and high commissions of using a real estate agent, or are in a tough situation and need to sell your house fast, R &amp; T Dwellings will remove the biggest obstacles you'll face.</p>
    <p class="about__text">We'll give you top dollar for your house, accept it in any condition, and take you through the whole process quickly. Our team is local and made up of licensed and insured home builders and real estate professionals who have a proven track record.</p>
    <ul class="contacts">
      <li><svg viewBox="0 0 10 10"><path d="M5 0a3.5 3.5 0 0 1 3.5 3.5C8.5 6 5 10 5 10S1.5 6 1.5 3.5A3.5 3.5 0 0 1 5 0z" fill="var(--green)"/></svg>P o box 829 Fernwick my 10472</li>
      <li><svg viewBox="0 0 10 10"><rect width="10" height="10" rx="2" fill="var(--green)"/><path d="M3 2.5l1 1.5-.6.8a4 4 0 0 0 1.8 1.8l.8-.6 1.5 1-.6 1C4.5 7.8 2.2 5.5 2 3.1z" fill="#fff"/></svg>555-214-8693</li>
      <li><svg viewBox="0 0 10 10"><rect y="2" width="10" height="6.5" fill="var(--green)"/><path d="M0 2l5 3.5L10 2" fill="none" stroke="#fff"/></svg>info@rntdwellings.example</li>
      <li><svg viewBox="0 0 10 10"><circle cx="5" cy="5" r="5" fill="var(--green)"/></svg>Rntdwellings.example</li>
    </ul>
  </div>
  <div class="stamp"></div>
</section>

</body>
</html>
```